Albeto Wine Label For Harbor Grove

Cedar Bend Winery is in need of a wine label for new wine being release. This wine will be used as a fundraiser for Harbor Grove, a chimpanzee santuary in Georgia. The label should reflect a high-end, classy image and the label should suggest the chimp philanthropy without specifically naming the organization (for legal purposes). The label can be a little whimsical without being too cartoonish or child like. This wine will be sold for $30 so it should project a sense of elegance too.
Updates

holiday season makes it difficult to get feedback necessary for approval. just need a few more days...

Industry/Entity Type

Winery

Font styles to use
Sans Serif

Requirements
Must have
• Label should show common design appearance as other labels downloaded.
• Label should be a dark (emerald) green color. Label should have wine name "Albeto" in center. Label should include an image or silhouette of a chimp on it
Should not have
• no cartoonish images;

```html
<!DOCTYPE html>
<html lang="en">
<head>
<meta charset="utf-8">
<title>Albeto – Cedar Bend Winery Label</title>
<link rel="stylesheet" href="https://fonts.googleapis.com/css2?family=Cinzel:wght@400;700&display=swap">
<style>
  :root {
    --page: #ffffff;
    --emerald: #034030;
    --emerald-light: #22634a;
    --emerald-mid: #0f4a33;
    --emerald-dark: #002a1a;
    --gold: #c8852a;
    --fur: #6b5a44;
  }
  html, body {
    margin: 0;
    padding: 0;
    width: 1200px;
    height: 805px;
    overflow: hidden;
    background: var(--page);
  }
  .label {
    display: block;
    width: 1200px;
    height: 805px;
  }
  .label text {
    font-family: "Cinzel", serif;
    fill: var(--gold);
  }
  .panel { fill: var(--emerald); }
  .frame { fill: none; stroke: var(--gold); stroke-width: 5; }
  .diamond-outer { fill: var(--emerald); }
  .diamond-gold { fill: var(--gold); }
  .diamond-inner { fill: var(--emerald); }
  .diamond-scene { fill: url(#scene); stroke: var(--gold); stroke-width: 3; }
  .rule { stroke: var(--gold); stroke-width: 2; opacity: .7; }
  .wine-name { font-size: 132px; text-anchor: middle; }
  .brand-name { font-size: 58px; font-weight: 700; text-anchor: middle; letter-spacing: 2px; }
  .stat { font-size: 24px; font-weight: 700; text-anchor: middle; }
  .cause { font-size: 28px; }
  .warning-title { font-size: 20px; font-weight: 700; }
  .warning-body { font-size: 20px; }
  .producer { font-size: 20px; text-anchor: middle; letter-spacing: 1px; }
  .producer-strong { font-size: 19px; font-weight: 700; text-anchor: middle; letter-spacing: 1px; }
  .web-box { fill: none; stroke: var(--gold); stroke-width: 2.5; }
  .web { font-size: 18px; font-weight: 700; text-anchor: middle; letter-spacing: 1px; }
  .emblem { fill: var(--gold); opacity: .9; }
  .portrait { fill: var(--fur); }
</style>
</head>
<body>
<svg class="label" viewBox="0 0 2000 1342" xmlns="http://www.w3.org/2000/svg">
  <defs>
    <linearGradient id="scene" x1="0" y1="0" x2="0" y2="1">
      <stop offset="0" stop-color="var(--emerald-light)"/>
      <stop offset="0.5" stop-color="var(--emerald-mid)"/>
      <stop offset="1" stop-color="var(--emerald-dark)"/>
    </linearGradient>
  </defs>

  <rect class="panel" x="115" y="198" width="1770" height="943"/>
  <rect class="frame" x="142" y="226" width="1716" height="888"/>

  <polygon class="diamond-outer" points="1000,60 1490,670 1000,1280 510,670"/>
  <polygon class="diamond-gold" points="1000,98 1445,670 1000,1242 555,670"/>
  <polygon class="diamond-inner" points="1000,135 1415,670 1000,1205 585,670"/>
  <polygon class="diamond-scene" points="1000,168 1390,670 1000,1172 610,670"
           role="img" aria-label="Misty green mountain range in the background"/>

  <ellipse class="portrait" cx="1000" cy="455" rx="108" ry="125"
           role="img" aria-label="Engraved portrait of a chimpanzee head"/>

  <line class="rule" x1="735" y1="627" x2="1265" y2="627"/>
  <text class="wine-name" x="1006" y="745" textLength="540" lengthAdjust="spacing">ALBETO</text>
  <line class="rule" x1="735" y1="773" x2="1265" y2="773"/>

  <text class="brand-name" x="1000" y="905">CEDAR</text>
  <text class="brand-name" x="1000" y="965">BEND</text>

  <rect class="emblem" x="240" y="293" width="146" height="146"
        transform="rotate(45 313 366)"
        role="img" aria-label="Emblem of sun, grapes, mountain and hills"/>

  <g transform="translate(288 1078) rotate(-90)">
    <text class="cause" x="0" y="0" textLength="560" lengthAdjust="spacingAndGlyphs">This wine will be used as a fundraiser</text>
    <text class="cause" x="0" y="33" textLength="480" lengthAdjust="spacingAndGlyphs">for Harbor Grove, a chimpanzee</text>
    <text class="cause" x="0" y="66" textLength="310" lengthAdjust="spacingAndGlyphs">santuary in Georgia.</text>
  </g>

  <text class="stat" x="703" y="1080">11.6% Alc/Vol</text>
  <text class="stat" x="1253" y="1080">750ml</text>

  <g transform="rotate(-90)">
    <text class="warning-title" x="-808" y="1567" textLength="293" lengthAdjust="spacingAndGlyphs">GOVERNMENT WARNING:</text>
    <text class="warning-body" x="-845" y="1627" textLength="530" lengthAdjust="spacingAndGlyphs">(1)  According to the Surgeon General, women</text>
    <text class="warning-body" x="-808" y="1657" textLength="528" lengthAdjust="spacingAndGlyphs">should not drink alcoholic beverages during</text>
    <text class="warning-body" x="-808" y="1687" textLength="521" lengthAdjust="spacingAndGlyphs">pregnancy because of the risk of birt deffects.</text>
    <text class="warning-body" x="-845" y="1717" textLength="542" lengthAdjust="spacingAndGlyphs">(2)  Consumption of alcoholic beverages impairs</text>
    <text class="warning-body" x="-808" y="1747" textLength="553" lengthAdjust="spacingAndGlyphs">your ability to drive a car or operate machinery,</text>
    <text class="warning-body" x="-808" y="1777" textLength="353" lengthAdjust="spacingAndGlyphs">and may cause health problems.</text>
  </g>
  <line class="rule" x1="1590" y1="415" x2="1590" y2="808"/>

  <text class="producer" x="1663" y="905">Produced &amp; bottled at</text>
  <text class="producer-strong" x="1663" y="935">CEDAR BEND RESORT</text>
  <text class="producer-strong" x="1663" y="965">&amp; SPA MILLBROOK GA</text>

  <rect class="web-box" x="1488" y="993" width="350" height="51"/>
  <text class="web" x="1663" y="1025">WWW.CEDARBENDGA.COM</text>

  <text class="producer" x="1663" y="1085">Contains Sulfites</text>
</svg>
</body>
</html>
```